Vortique Energy Business Card Design

website: www.vortiqueenergy.example
Project: Business Card Design for Vortique Energy
Name: Derek Holloway
Title: Founder / Operations Strategist
Visual Identity & Logo:
Logo File: VRT-Logo-FullGradient-Final.png (Attached).
Color Palette: The brand relies on a distinctive Cyan (Blue) to Lime Green gradient.
Background Preference: We want a Dark Mode aesthetic (Deep Matte Black, Charcoal, or Dark Slate) to make the neon gradient of the logo pop. This feels more "tech/industrial" than a standard white card.
Design Aesthetic (The "Ops" Vibe):
Concept: "Grid & Infrastructure." We are a solar rental company, focusing on logistics and access.
Typography: White, bold sans-serif text for contact info. High contrast against the dark background.
Accents: Use the Cyan or Lime Green from the logo for thin divider lines or edge painting.
Avoid: No orange/gold (clashes with logo). No cartoon leaves.
Layout Requirements:
Front: Large, centered logo. Maybe a subtle UV gloss spot varnish over the logo icon.
Back: Name, Title, Contact Info.
Texture: Matte finish cardstock with gloss elements.
sample mock up of information on card: https://brimtolcorp-my.filedock.example/:i:/g/personal/derek_holloway_vortiqueenergy_com/AbCdEfGhIjKlMnOpQrStUvWxYz0123456789AbCdEfGh?e=X1Y2Z3
Logo: https://brimtolcorp.filedock.example/:i:/s/VortiqueEnergy/ZyXwVuTsRqPoNmLkJiHgFeDcBa9876543210ZyXwVuTs?e=Q4R5S6

```html
<!DOCTYPE html>
<html lang="en">
<head>
<meta charset="UTF-8">
<title>Vortique Energy – Business Card</title>
<link rel="stylesheet" href="https://fonts.googleapis.com/css2?family=Arimo:wght@400;700&display=swap">
<style>
  :root {
    --backdrop: #3d3d3d;
    --card: #2c2c2c;
    --card-back: #2a2a2a;
    --cyan: #1aa9d4;
    --teal: #22c4c9;
    --lime: #b4dc26;
    --white: #f2f2f2;
    --rule: #5a5a5a;
    --emboss: #8a8a8a;
  }
  * { margin: 0; padding: 0; box-sizing: border-box; }
  html, body {
    width: 1200px; height: 1200px; overflow: hidden;
    background: var(--backdrop);
    font-family: "Arimo", Arial, sans-serif;
  }
  .card {
    position: absolute;
    width: 688px; height: 394px;
    border-radius: 18px;
    overflow: hidden;
  }
  .card--front { left: 267px; top: 158px; background: var(--card); }
  .card--back { left: 263px; top: 652px; background: var(--card-back); }

  .brand {
    position: absolute;
    display: flex; align-items: center; gap: 10px;
  }
  .brand__mark { width: 22px; height: 22px; background: var(--teal); }
  .brand__name { color: var(--teal); font-size: 27px; font-weight: 400; white-space: nowrap; }
  .card--front .brand { left: 83px; top: 180px; }

  .divider {
    position: absolute; left: 361px; top: 81px;
    width: 1px; height: 236px;
    background: linear-gradient(to bottom, transparent, var(--rule) 15%, var(--rule) 85%, transparent);
  }
  .contact { position: absolute; left: 386px; top: 102px; color: var(--white); }
  .contact__name { color: var(--cyan); font-weight: 700; font-size: 26px; line-height: 30px; }
  .contact__title { font-size: 15px; line-height: 18px; margin-top: 1px; }
  .contact__address { font-size: 16px; line-height: 20.5px; margin-top: 20px; }
  .contact__lines { margin-top: 17px; font-size: 16px; line-height: 20.5px; }
  .contact__line { display: flex; align-items: center; }
  .contact__icon { width: 16px; height: 16px; margin-right: 10px; margin-left: -3px; }

  .edge {
    position: absolute; left: 0; right: 0; bottom: 0; height: 7px;
    background: linear-gradient(to right, var(--cyan), var(--lime));
  }

  .card--back .brand { left: 0; right: 0; top: 150px; justify-content: center; gap: 16px; }
  .card--back .brand__mark { width: 40px; height: 40px; background: #1b1b1b; }
  .card--back .brand__name { color: var(--emboss); font-size: 52px; }

  .tagline {
    position: absolute; left: 0; right: 0; top: 330px;
    text-align: center; font-size: 18px;
    background: linear-gradient(to right, var(--cyan), var(--lime));
    -webkit-background-clip: text; background-clip: text; color: transparent;
  }
</style>
</head>
<body>
  <section class="card card--front">
    <div class="brand">
      <span class="brand__mark"></span>
      <span class="brand__name">Vortique Energy</span>
    </div>
    <div class="divider"></div>
    <div class="contact">
      <div class="contact__name">Derek Holloway</div>
      <div class="contact__title">Founder / Operations Strategist</div>
      <div class="contact__address">
        Vortique Energy<br>
        4120 Marlow Ridge Way<br>
        Castlebrook, FL 30417
      </div>
      <div class="contact__lines">
        <div class="contact__line">
          <svg class="contact__icon" viewBox="0 0 24 24" aria-hidden="true">
            <path fill="#b4dc26" d="M6.6 10.8c1.4 2.8 3.8 5.1 6.6 6.6l2.2-2.2c.3-.3.7-.4 1-.2 1.1.4 2.3.6 3.6.6.6 0 1 .4 1 1V20c0 .6-.4 1-1 1C10.6 21 3 13.4 3 4c0-.6.4-1 1-1h3.5c.6 0 1 .4 1 1 0 1.3.2 2.5.6 3.6.1.3 0 .7-.2 1l-2.3 2.2z"/>
          </svg>
          555.014.2290
        </div>
        <div class="contact__line">
          <svg class="contact__icon" viewBox="0 0 24 24" aria-hidden="true">
            <circle cx="12" cy="12" r="10" fill="#b4dc26"/>
            <path fill="#2c2c2c" d="M8 5c2 1 1 3 3 3s1 3-1 3-3 2-1 4-1 4-2 3c-2-2-3-5-2-8 1-2 2-4 4-5zm8 3c1 1 2 3 1 5s-3 2-3 4-1 2-2 1c0-2 1-3 0-4s1-3 2-3 1-2 2-3z"/>
          </svg>
          www.vortiqueenergy.example
        </div>
      </div>
    </div>
    <div class="edge"></div>
  </section>

  <section class="card card--back">
    <div class="brand">
      <span class="brand__mark"></span>
      <span class="brand__name">Vortique Energy</span>
    </div>
    <p class="tagline">No debt, no liens, no maintenance, just savings</p>
  </section>
</body>
</html>
```